Family owned plumbing contractor needs eye catching business card design

Business cards that are unique, eye catching, and provide customers with general company information, such as name, address, phone number, website, employee name/title, cell phone #, & email address. We are transitioning to a new logo that utilizes a more retro feel, so we are interested in seeing some cool old school designs in the mix. We are liking the dark background on some of the samples on this website. If that is workable with our artwork, we would like to see that incorporated into the design.
Contact Information for Business Card
Copperline Pipeworks, Inc.
www.copperlinepipeworks.example
(555) 392-7068 phone
Nevada License #64205
California License #5810473
Dale Wrennick, President
(555) 618-9032 cell
dale@copperlinepipeworks.example
Residential * Commercial * Service
Requirements
Must have
- The business card details listed above & logo provided.
Nice to have
- I made some notes about color options in the description.

```html
<!DOCTYPE html>
<html lang="en">
<head>
<meta charset="utf-8">
<title>Copperline Pipeworks, Inc. – Business Card</title>
<link href="https://fonts.googleapis.com/css2?family=Open+Sans:wght@400;600;700;800&display=swap" rel="stylesheet">
<style>
  :root {
    --stage: #2b2b2d;
    --card-dark: #1c1c1e;
    --card-dark-2: #2a2a2c;
    --mint: #8fd6cb;
    --paper: #f2f3f2;
    --steel: #6f95ad;
    --ink-light: #e9ecec;
    --ink-soft: #c9cfcf;
  }
  * { box-sizing: border-box; margin: 0; padding: 0; }
  html, body { width: 1200px; height: 914px; overflow: hidden; }
  body {
    background: var(--stage);
    font-family: "Open Sans", Arial, sans-serif;
    display: flex;
    align-items: center;
    justify-content: center;
    gap: 40px;
  }
  .card {
    width: 540px;
    height: 309px;
    position: relative;
    overflow: hidden;
    box-shadow: 0 14px 30px rgba(0,0,0,.45);
  }

  /* Front */
  .card-front { background: var(--mint); padding: 12px; }
  .front-frame {
    width: 100%; height: 100%;
    border: 5px solid var(--paper);
    position: relative;
  }
  .front-texture {
    position: absolute; inset: 0;
    background: radial-gradient(ellipse at 55% 40%, var(--card-dark-2), var(--card-dark) 70%);
  }
  .front-content {
    position: absolute; inset: 0;
    display: flex; flex-direction: column; align-items: center; justify-content: center;
    text-align: center;
  }
  .brand-mark {
    width: 50px; height: 50px; border-radius: 50%;
    background: var(--steel);
  }
  .brand-name {
    color: var(--ink-light);
    font-weight: 800;
    font-size: 26px;
    letter-spacing: .5px;
    margin-top: 12px;
  }
  .service-line {
    color: var(--mint);
    font-size: 12px;
    font-weight: 600;
    letter-spacing: 2px;
    text-transform: uppercase;
    margin-top: 6px;
  }
  .front-address {
    color: var(--ink-light);
    font-size: 14px;
    font-weight: 600;
    letter-spacing: 1px;
    margin-top: 22px;
  }
  .licenses {
    color: var(--ink-soft);
    font-size: 12px;
    letter-spacing: .6px;
    margin-top: 6px;
  }

  /* Back */
  .card-back { background: var(--paper); }
  .back-dark {
    position: absolute; inset: 0;
    background: radial-gradient(ellipse at 30% 50%, var(--card-dark-2), var(--card-dark) 75%);
    clip-path: polygon(0 0, 48% 0, 48% 42%, 62% 72%, 62% 100%, 0 100%);
  }
  .back-stripe { position: absolute; inset: 0; width: 100%; height: 100%; }
  .holder { position: absolute; left: 40px; top: 48px; }
  .holder-name {
    color: var(--mint);
    font-size: 20px; font-weight: 400; letter-spacing: 1.5px;
    text-transform: uppercase;
  }
  .holder-title { color: var(--ink-soft); font-size: 14px; margin-top: 2px; }
  .contact-list {
    position: absolute; left: 40px; bottom: 38px;
    list-style: none;
    display: flex; flex-direction: column; gap: 8px;
  }
  .contact-list li {
    display: flex; align-items: center; gap: 10px;
    color: var(--ink-light); font-size: 13.5px; letter-spacing: .4px;
  }
  .contact-list svg { width: 15px; height: 15px; flex: none; }
  .back-brand {
    position: absolute; right: 28px; top: 70px; width: 200px;
    display: flex; flex-direction: column; align-items: center;
    text-align: center;
  }
  .back-brand .brand-mark { width: 52px; height: 52px; }
  .back-brand .brand-name { color: var(--steel); font-size: 20px; line-height: 1.25; }
</style>
</head>
<body>

<section class="card card-front" aria-label="Business card front">
  <div class="front-frame">
    <div class="front-texture" role="img" aria-label="Dark distressed crackle texture background"></div>
    <div class="front-content">
      <span class="brand-mark"></span>
      <span class="brand-name">Copperline Pipeworks, Inc.</span>
      <span class="service-line">Residential * Commercial * Service</span>
      <p class="front-address">48 Harbor Lane, Lakeview, NV 89501</p>
      <p class="licenses">Nevada License #64205 &nbsp;|&nbsp; California License #5810473</p>
    </div>
  </div>
</section>

<section class="card card-back" aria-label="Business card back">
  <div class="back-dark" role="img" aria-label="Dark distressed crackle texture background"></div>
  <svg class="back-stripe" viewBox="0 0 540 309" preserveAspectRatio="none" aria-hidden="true">
    <polyline points="259,0 259,130 335,222 335,309" fill="none" stroke="#8fd6cb" stroke-width="6"/>
  </svg>

  <div class="holder">
    <p class="holder-name">Dale Wrennick</p>
    <p class="holder-title">President</p>
  </div>

  <ul class="contact-list">
    <li>
      <svg viewBox="0 0 16 16" aria-hidden="true"><rect x="4" y="1" width="8" height="14" rx="1.5" fill="none" stroke="#8fd6cb" stroke-width="1.4"/><circle cx="8" cy="12.5" r=".9" fill="#8fd6cb"/></svg>
      (555) 618-9032
    </li>
    <li>
      <svg viewBox="0 0 16 16" aria-hidden="true"><path d="M4 2l2.5 3-1.5 1.5c.8 1.8 2.2 3.2 4 4L10.5 9 13.5 11.5 12 14C7 14 2 9 2 4z" fill="#8fd6cb"/></svg>
      (555) 392-7068
    </li>
    <li>
      <svg viewBox="0 0 16 16" aria-hidden="true"><rect x="1" y="3" width="14" height="10" fill="#8fd6cb"/><polyline points="1,3 8,9 15,3" fill="none" stroke="#1c1c1e" stroke-width="1.3"/></svg>
      dale@copperlinepipeworks.example
    </li>
    <li>
      <svg viewBox="0 0 16 16" aria-hidden="true"><circle cx="8" cy="8" r="6.5" fill="#8fd6cb"/><g fill="none" stroke="#1c1c1e" stroke-width="1"><ellipse cx="8" cy="8" rx="2.6" ry="6.5"/><line x1="1.5" y1="8" x2="14.5" y2="8"/></g></svg>
      www.copperlinepipeworks.example
    </li>
  </ul>

  <div class="back-brand">
    <span class="brand-mark"></span>
    <span class="brand-name">Copperline Pipeworks, Inc.</span>
  </div>
</section>

</body>
</html>
```